MD Business Card

I want to create a simple business card.
I am a consultant. I design and develop furniture, lighting and accessories for hospitality and retail brands.
I want the card to be simple and clean. Not too much of a logo - but it needs the basic information shown on the attached file.
Also - I have shown some fonts that I like on the attached file.
The card can be square or rectangle. It should be double sided.
I prefer 1-2 colors (not too colorful - but using color an an accent) Even if using color on the edges as an accent.

My snapquilt link shows some other graphics styles that I like. I like clean and simple.
http://www.snapquilt.com/marendowsett/business-cards/

Reason: I needed a few more days to see some of the options evolve.

Hospitality

```html
<!DOCTYPE html>
<html lang="en">
<head>
<meta charset="utf-8">
<title>Maren Dowsett – Business Card</title>
<link rel="stylesheet" href="https://fonts.googleapis.com/css2?family=Arimo:wght@400&family=Jost:wght@300&display=swap">
<style>
  :root {
    --ink: #1a1a1a;
    --accent: #9e8c8c;
    --paper: #ffffff;
    --frame-grey: #8a8a8a;
  }
  * { margin: 0; padding: 0; box-sizing: border-box; }
  html, body {
    width: 1200px;
    height: 650px;
    overflow: hidden;
    background: var(--paper);
  }
  .canvas {
    position: relative;
    width: 1200px;
    height: 650px;
    background: var(--paper);
  }

  /* Front of card */
  .card-front {
    position: absolute;
    left: 30px;
    top: 40px;
    width: 556px;
    height: 562px;
    border: 1px solid var(--frame-grey);
    background: var(--paper);
  }
  .card-front__frame {
    position: absolute;
    left: 13px;
    top: 16px;
    width: 529px;
    height: 529px;
    border: 4px solid var(--ink);
    border-radius: 20px;
  }
  .name-line {
    position: absolute;
    font-family: "Arimo", Arial, sans-serif;
    font-weight: 400;
    font-size: 54px;
    line-height: 1;
    color: var(--accent);
    white-space: nowrap;
  }
  .name-line--first { left: 200px; top: 160px; }
  .name-line--last  { left: 310px; top: 306px; }
  .tagline {
    position: absolute;
    left: 0;
    right: 0;
    top: 455px;
    text-align: center;
    font-family: "Jost", "Century Gothic", sans-serif;
    font-weight: 300;
    font-size: 34px;
    color: var(--ink);
  }

  /* Back of card */
  .card-back {
    position: absolute;
    left: 632px;
    top: 42px;
    width: 556px;
    height: 560px;
    border: 8px solid var(--ink);
    background: var(--paper);
  }
  .contact {
    position: absolute;
    left: 29px;
    top: 52px;
    font-family: "Jost", "Century Gothic", sans-serif;
    font-weight: 300;
    color: var(--ink);
    line-height: 1.12;
  }
  .contact__email { font-size: 32px; display: block; }
  .contact__phone { font-size: 37px; display: block; letter-spacing: 0.5px; }
  .services {
    position: absolute;
    left: 24px;
    right: 10px;
    bottom: 18px;
    font-family: "Arimo", Arial, sans-serif;
    font-weight: 400;
    font-size: 30px;
    color: var(--ink);
    white-space: nowrap;
  }
  .services__dot { font-size: 22px; vertical-align: 3px; margin: 0 5px; }
</style>
</head>
<body>
  <main class="canvas">
    <section class="card-front" aria-label="Card front">
      <div class="card-front__frame"></div>
      <p class="name-line name-line--first">Maren</p>
      <p class="name-line name-line--last">Dowsett</p>
      <p class="tagline">hospitality &amp; home</p>
    </section>

    <section class="card-back" aria-label="Card back">
      <p class="contact">
        <span class="contact__email">maren@marendowsett.com</span>
        <span class="contact__phone">555.014.2270</span>
      </p>
      <p class="services">ff&amp;e<span class="services__dot">•</span>furniture<span class="services__dot">•</span>lighting<span class="services__dot">•</span>textiles<span class="services__dot">•</span>etc</p>
    </section>
  </main>
</body>
</html>
```